Brand new letterhead, business card, email signature etc.

We are a financial company in London, UK. Our website is www.quorvane.com. We're wanting a complete remodel of the company colours, letter head, business cards, email signatures, etc. Looking to keep the same font for the company name. I have upload a colour palette that we want to work with. We're looking for company letterhead for outgoing letters/ correspondence, letterhead for internal documentation, email signatures, e-letters. etc. Ultimately we will redesign the entire website also. It is important that our clients get a strong, secure, warm, trustworthy, solid feeling and first impression.
Updates

Designs look the same

Target Market(s)

Institutional investors, (ultra) high net worth individuals

Industry/Entity Type

Finance, Invesments banking.

Font styles to use
Other font styles liked:
• Current font is "Champagne & Limousines"

Requirements
Must have
• Must use the colours provided on the PDF uploaded to the portal. The purple = main colour. The red = accent colour.
Nice to have
• Nice to use same font as now for the company name "Marlowin". Font is "Champagne & Limousines". Nice to have some reference to the old logo flower, but only subtle.
Should not have
• Do not use the colour red from our website. Use the colours provided on the colour palette PDF that I uploaded in the portal.

```html
<!DOCTYPE html>
<html lang="en">
<head>
<meta charset="utf-8">
<title>Marlowin Stationery – Presentation Folder</title>
<link href="https://fonts.googleapis.com/css2?family=Jost:wght@300;400;500&display=swap" rel="stylesheet">
<style>
  :root{
    --paper:#fcfbfa;
    --canvas:#ffffff;
    --rule:#8d8a8b;
    --strip:#d8d3d5;
    --accent:#f2a48c;
    --ink:#4f4448;
    --bloom-grey-a:#f4f2f2;
    --bloom-grey-b:#e2dddf;
    --bloom-pink-a:#fbe6de;
    --bloom-pink-b:#ebe6e3;
  }
  *{box-sizing:border-box;margin:0;padding:0}
  html,body{width:999px;height:1200px;overflow:hidden;background:var(--canvas)}
  body{position:relative;font-family:"Jost",sans-serif;color:var(--ink)}
  .abs{position:absolute}
  .sheet{background:var(--paper)}
  .frames{position:absolute;left:0;top:0}
  .bloom-head{background:linear-gradient(160deg,var(--bloom-grey-a),var(--bloom-grey-b))}
  .bloom-band{background:linear-gradient(180deg,var(--bloom-pink-a),var(--bloom-pink-b))}
  .wordmark{display:flex;align-items:center;gap:6px}
  .wordmark .mark{width:22px;height:22px;border:1px solid var(--rule)}
  .wordmark .name{font-weight:300;font-size:12.5px;letter-spacing:1.6px;text-transform:uppercase;color:var(--ink)}
  .contacts{font-size:6px;line-height:7.5px;color:var(--ink);font-weight:400}
  .contacts li{list-style:none;position:relative;padding-left:8px;margin-bottom:3px}
  .contacts li::before{content:"";position:absolute;left:0;top:1px;width:4px;height:5px;border:1px solid var(--accent);border-radius:2px 2px 0 0}
  .tagline{font-size:9.5px;line-height:13px;color:var(--accent);text-transform:uppercase;letter-spacing:0;font-weight:400;white-space:nowrap}
  .web{font-size:7.5px;font-weight:500;color:var(--ink)}
  .mini .mark{width:14px;height:14px}
  .mini .name{font-size:9px;letter-spacing:1.2px}
  .micro{font-size:3.4px;line-height:5px}
  .micro li{padding-left:6px;margin-bottom:1px}
  .micro li::before{width:3px;height:3px;top:.5px}
  .card-name{font-size:6.5px;text-transform:uppercase;color:var(--ink)}
  .card-role{font-size:3.6px;color:var(--accent)}
</style>
</head>
<body>

<!-- Outer folder, front -->
<div class="abs sheet" style="left:187px;top:135px;width:625px;height:439px"></div>
<div class="abs" style="left:187px;top:135px;width:12px;height:439px;background:var(--strip)"></div>
<div class="abs" style="left:500px;top:135px;width:10px;height:439px;background:var(--strip)"></div>

<div class="abs bloom-head" role="img" aria-label="Line illustration of a lily flower with stamens" style="left:358px;top:135px;width:142px;height:129px"></div>
<div class="abs bloom-band" role="img" aria-label="Repeated lily line pattern in soft coral and grey" style="left:358px;top:264px;width:142px;height:91px"></div>
<div class="abs bloom-head" role="img" aria-label="Line illustration of a lily flower with stamens" style="left:671px;top:135px;width:141px;height:129px"></div>
<div class="abs bloom-band" role="img" aria-label="Repeated lily line pattern in soft coral and grey" style="left:671px;top:264px;width:141px;height:91px"></div>

<div class="abs wordmark" style="left:252px;top:209px"><span class="mark"></span><span class="name">Marlowin</span></div>
<div class="abs wordmark" style="left:565px;top:209px"><span class="mark"></span><span class="name">Marlowin</span></div>

<ul class="abs contacts" style="left:214px;top:352px;width:140px">
  <li>Marlowin Trust Limited, Arden House, Douglas, Isle of Man, IM1 4QT</li>
  <li>Marlowin Group Limited, 9th Floor, 14 Fenner Lane, London, EC2M 7PL</li>
  <li>info@quorvane.com</li>
</ul>

<p class="abs tagline" style="left:252px;top:437px">Dedicated<br>Mid-market<br>Specialists</p>
<p class="abs tagline" style="left:565px;top:437px">A contemporary<br>broker with<br>traditional<br>ideas about service</p>

<p class="abs web" style="left:252px;top:531px">www.quorvane.com</p>
<p class="abs web" style="left:565px;top:531px">www.quorvane.com</p>

<!-- Inner folder, open -->
<div class="abs sheet" style="left:187px;top:613px;width:625px;height:439px"></div>
<div class="abs" style="left:187px;top:613px;width:12px;height:439px;background:var(--strip)"></div>
<div class="abs" style="left:500px;top:613px;width:10px;height:439px;background:var(--strip)"></div>
<div class="abs bloom-head" role="img" aria-label="Line illustration of a lily flower with stamens" style="left:358px;top:613px;width:142px;height:129px"></div>
<div class="abs bloom-band" role="img" aria-label="Repeated lily line pattern in soft coral and grey" style="left:358px;top:742px;width:142px;height:113px"></div>
<p class="abs tagline" style="left:358px;top:926px">Expert commentary<br>from accomplished<br>market professionals</p>

<!-- Letterhead in pocket -->
<div class="abs" style="left:508px;top:630px;width:304px;height:127px;background:var(--paper)"></div>
<div class="abs" style="left:508px;top:697px;width:8px;height:60px;background:var(--strip)"></div>
<div class="abs bloom-head" role="img" aria-label="Small lily line illustration" style="left:760px;top:630px;width:52px;height:67px"></div>
<div class="abs wordmark mini" style="left:530px;top:661px"><span class="mark"></span><span class="name">Marlowin</span></div>
<ul class="abs contacts micro" style="left:655px;top:675px;width:104px">
  <li>Marlowin Trust Limited, Arden House, Douglas, IM1 4QT</li>
  <li>Marlowin Group Limited, 14 Fenner Lane, London, EC2M 7PL</li>
  <li>info@quorvane.com</li>
</ul>

<!-- Business card -->
<div class="abs" style="left:572px;top:958px;width:88px;height:82px;background:var(--paper)"></div>
<div class="abs bloom-head" role="img" aria-label="Small lily line illustration" style="left:630px;top:958px;width:30px;height:45px"></div>
<div class="abs wordmark mini" style="left:597px;top:966px"><span class="mark" style="width:12px;height:12px"></span><span class="name" style="font-size:8px">Marlowin</span></div>
<p class="abs card-name" style="left:597px;top:988px">Elena Corby</p>
<p class="abs card-role" style="left:597px;top:996px">Head of Client Relations</p>
<ul class="abs contacts micro" style="left:592px;top:1008px;width:64px">
  <li>Marlowin Trust Limited, Arden House, Douglas, IM1 4QT</li>
  <li>Marlowin Group Limited, 14 Fenner Lane, London, EC2M 7PL</li>
  <li>info@quorvane.com</li>
</ul>

<svg class="frames" width="999" height="1200" viewBox="0 0 999 1200" fill="none" stroke="var(--rule)" stroke-width="0.8">
  <rect x="187" y="135" width="625" height="439"/>
  <line x1="201.5" y1="135" x2="201.5" y2="574" stroke="var(--accent)"/>
  <line x1="512.5" y1="135" x2="512.5" y2="574" stroke="var(--accent)"/>
  <line x1="358" y1="135" x2="358" y2="574"/>
  <line x1="671" y1="135" x2="671" y2="574"/>
  <line x1="199" y1="264" x2="500" y2="264"/>
  <line x1="510" y1="264" x2="812" y2="264"/>
  <line x1="358" y1="304" x2="500" y2="304" stroke-width="0.5"/>
  <line x1="671" y1="304" x2="812" y2="304" stroke-width="0.5"/>

  <rect x="187" y="613" width="625" height="439"/>
  <line x1="201.5" y1="613" x2="201.5" y2="1052" stroke="var(--accent)"/>
  <path d="M358 728 H277 V983 H500"/>
  <path d="M358 613 V855"/>
  <line x1="358" y1="742" x2="500" y2="742" stroke-width="0.5"/>
  <line x1="358" y1="790" x2="500" y2="790" stroke-width="0.5"/>

  <rect x="508" y="630" width="304" height="127"/>
  <line x1="508" y1="697" x2="812" y2="697" stroke-width="0.5"/>
  <path d="M738 1052 V732 L760 718"/>
  <path d="M500 1052 L513 983 H757 L790 997 L812 1052"/>

  <path d="M572 1040 V958 H660 V1040 Z" stroke-width="0.6"/>
  <line x1="572" y1="1003" x2="660" y2="1003" stroke-width="0.5"/>
</svg>

</body>
</html>
```